Website for the K7VANT-Lab research laboratory.

We are a research team working on personality disorders. We would like a website that presents the team members (noting that students change frequently), ongoing projects with active recruitments, the latest publications, student resources, and possibly patient resources.

We have already prepared the logo with Plumvetta.

Our research areas:
1- Lifestyle Medicine and BPD
This area focuses on understanding lifestyle habits and their impact on the health of individuals living with Borderline Personality Disorder (BPD). It aims to improve essential components such as sleep, physical activity, and nutrition by identifying and promoting favorable lifestyle habits. The goal is to strengthen emotional regulation and improve overall health by fully integrating the physical dimension into recovery.
2- Interventions Supporting Psychosocial Functioning
Develop the full recovery potential and enhance social and professional integration strategies to support the life journey of patients in all its dimensions. This area focuses on practices and interventions that facilitate a return to an active life and harmonious integration into society.
3- Optimization of Psychotherapeutic Strategies in BPD
Optimize psychotherapeutic approaches for BPD by identifying the most effective methods, adapting them to individual needs, and evaluating their long-term impact. This research area aims to refine and personalize treatments to maximize their therapeutic benefits.
4- Biological Treatments for BPD: Neuromodulation and Pharmacotherapy
Develop and evaluate biological treatments, particularly in neuromodulation and pharmacotherapy, to improve the management of BPD. This area aims to explore scientific advances in these fields to offer complementary and innovative therapeutic options.

Vision
Affiliated with TVOLBAE, our laboratory is dedicated to creating tomorrow's interventions to offer a hopeful future for individuals living with Borderline Personality Disorder. We design and develop innovative solutions that integrate and value each individual, their loved ones, and their community, supporting their personal, social, functional, and physical recovery.

Values

Innovation
Our commitment to innovation guides every step of our research and development. We continually strive to push the boundaries of knowledge and techniques to create new and bold therapeutic solutions tailored to the evolving needs of individuals living with Borderline Personality Disorder.
Hope
We carry the hope of making a real difference in the lives of people living with BPD. This hope drives our work, pushing us to explore therapeutic approaches that offer patients a better and more serene future. By integrating this hope into our research, we are committed to developing interventions that inspire and support the recovery process. Through our research work, we wish to instill and spread hope.
Empathy and Personalization
We believe in a person-centered and inclusive approach where each individual is considered in their uniqueness and with compassion. By actively integrating patients and their experiences into our research, we aim to design solutions that not only meet their specific needs but also value their recovery while respecting their values. We wish to improve the satisfaction of individuals within the care network, promote the integration of their loved ones and their community.

```html
<!DOCTYPE html>
<html lang="en">
<head>
<meta charset="utf-8">
<title>K7VANT-Lab — BPD Research</title>
<link rel="stylesheet" href="https://fonts.googleapis.com/css2?family=Inter:wght@400;500;600;700&display=swap">
<style>
:root{
  --stage:#0d0d0d;
  --blue:#0a86cf;
  --blue-dark:#0670b0;
  --green:#3dbb48;
  --green-light:#5fd160;
  --ink:#111418;
  --muted:#4a4f56;
  --line:#d7dbe0;
  --white:#ffffff;
}
*{box-sizing:border-box;margin:0;padding:0}
html,body{width:1200px;height:2602px;overflow:hidden}
body{background:var(--stage);font-family:"Inter",Arial,sans-serif;color:var(--ink)}
.page{position:absolute;left:275px;top:0;width:651px;height:2602px;background:var(--white);overflow:hidden}
a{color:inherit;text-decoration:none}
.btn{display:inline-flex;align-items:center;justify-content:center;gap:8px;border-radius:20px;font-size:7.5px;font-weight:500;height:22px;padding:0 16px;color:var(--white)}
.btn-green{background:var(--green)}
.btn-blue{background:var(--blue)}
.btn-dark{background:var(--ink)}

/* header */
.site-header{height:63px;display:flex;align-items:center;justify-content:space-between;padding:0 35px}
.brand{display:flex;align-items:center;gap:6px;font-size:17px;font-weight:600;color:var(--blue)}
.brand-dot{width:20px;height:20px;border-radius:50%;background:var(--green)}
.nav{display:flex;gap:28px;font-size:7.5px;color:var(--ink)}

/* hero */
.hero{position:relative;height:287px;background:linear-gradient(90deg,#f4f8fa 0%,#e6eef2 45%,#c9d6de 100%)}
.hero-photo{position:absolute;right:0;top:0;width:360px;height:287px;background:linear-gradient(100deg,rgba(240,245,248,0) 0%,#b9c8d3 30%,#6f8293 70%,#8b9aa6 100%)}
.hero-text{position:relative;padding:52px 35px 0}
.hero h1{font-size:15px;line-height:22px;font-weight:700;width:250px}
.hero p{font-size:7px;line-height:13.5px;width:230px;margin-top:30px}
.hero .actions{display:flex;gap:14px;margin-top:28px}

/* about */
.about{height:350px;background:var(--blue);display:flex;gap:50px;padding:55px 35px 0}
.about-photo{width:248px;height:239px;background:linear-gradient(135deg,#e8eef2,#9fb6c7 60%,#5f89ad);border-radius:6px}
.about-body{color:var(--white);width:270px;padding-top:8px}
.about-body h2{font-size:14px;font-weight:700}
.about-body p{font-size:7px;line-height:13.5px;margin-top:10px}
.values{display:flex;gap:8px;margin-top:16px}
.value{background:var(--blue-dark);border-radius:4px;height:60px;display:flex;flex-direction:column;align-items:center;justify-content:center;gap:6px;font-size:7px;font-weight:600;text-align:center;padding:0 10px;min-width:69px}
.value svg{width:12px;height:12px}
.about .btn{margin-top:30px}

/* research */
.research{height:351px;background:linear-gradient(180deg,#f0f5f9,#ffffff);text-align:center;padding-top:25px}
.research h2{font-size:14px;font-weight:700}
.research .lead{font-size:7px;line-height:13.5px;width:330px;margin:16px auto 0}
.research .btn{margin-top:12px;padding:0 24px}
.areas{display:flex;gap:14px;padding:0 35px;margin-top:26px}
.area{flex:1;height:176px;border:1.5px solid #8fdd92;border-radius:3px;padding:14px 6px 0;background:var(--white)}
.area.active{background:var(--green);border-color:var(--green);color:var(--white)}
.area-art{width:56px;height:52px;margin:0 auto;border-radius:50%;background:radial-gradient(circle,#8cc6ea 0%,#d9ecf7 70%,rgba(255,255,255,0) 100%)}
.area.active .area-art{background:radial-gradient(circle,#2c8fd0 0%,#8fd79a 70%,rgba(61,187,72,0) 100%)}
.area h3{font-size:7px;line-height:11px;font-weight:700;margin-top:12px}
.area p{font-size:6.8px;line-height:13.5px;margin-top:10px;color:var(--muted)}
.area.active p{color:var(--white)}

/* team */
.team{position:relative;height:350px;background:radial-gradient(circle at 70% 20%,var(--green-light),var(--green) 55%);color:var(--white);padding:55px 35px 0}
.team h2{font-size:14px;font-weight:700}
.team-head{display:flex;justify-content:space-between;align-items:flex-end}
.team-head p{font-size:7px;line-height:13.5px;width:230px;margin-top:14px}
.team .btn{margin-bottom:2px}
.members{display:flex;gap:14px;margin-top:26px}
.member{flex:1;height:166px;position:relative;border-radius:4px;overflow:hidden}
.member .shot{position:absolute;inset:0}
.member .cap{position:absolute;left:0;right:0;bottom:0;height:38px;background:rgba(255,255,255,.55);padding:7px 8px;color:var(--ink)}
.member .cap b{display:block;font-size:8.5px}
.member .cap span{font-size:7px;color:var(--muted)}
.arrow{position:absolute;top:285px;width:10px;height:10px}

/* publications */
.pubs{height:350px;padding:32px 35px 0;background:#fafcfd}
.pubs-head{display:flex;justify-content:space-between;align-items:center}
.pubs h2{font-size:14px;font-weight:700}
.pub-grid{display:grid;grid-template-columns:repeat(3,1fr);column-gap:14px;row-gap:26px;margin-top:20px}
.pub{border-top:2px solid var(--line);padding-top:12px;height:116px;position:relative}
.pub.current{border-top-color:var(--blue)}
.pub h3{font-size:8px;line-height:10px;font-weight:700}
.pub p{font-size:6.8px;line-height:13.5px;margin-top:7px}
.pub a{position:absolute;bottom:0;font-size:7px;font-weight:600;color:var(--blue);display:flex;align-items:center;gap:5px}

/* projects */
.projects{position:relative;height:356px;background:linear-gradient(135deg,#0b86cf,#0a7cc2 50%,#3b9fd9);display:flex;padding:30px 35px 0;color:var(--white)}
.projects-intro{width:200px}
.projects-intro h2{font-size:14px;font-weight:700}
.projects-intro p{font-size:7px;line-height:13.5px;margin-top:14px;width:175px}
.doctor{position:absolute;left:35px;bottom:0;width:175px;height:205px;background:linear-gradient(180deg,rgba(255,255,255,0) 0%,rgba(240,244,248,.45) 40%,rgba(230,236,242,.8) 100%)}
.project-list{flex:1;display:flex;flex-direction:column;gap:8px}
.project{background:var(--white);color:var(--ink);border-radius:3px;padding:8px;height:74px}
.project.short{height:64px}
.project-top{display:flex;align-items:center;font-size:6.5px;color:var(--muted)}
.project-top b{font-size:8px;color:var(--ink);flex:1}
.project-top .k{margin-left:14px}
.project-top .v1{color:var(--blue);margin-left:6px}
.project-top .v2{color:var(--green);margin-left:6px}
.project-body{display:flex;align-items:center;justify-content:space-between;gap:12px;margin-top:8px;border-top:1px solid #e6e9ec;padding-top:6px}
.project-body p{font-size:6.8px;line-height:13.5px;width:260px}
.project-body .btn{padding:0 14px;white-space:nowrap}
.fade{position:absolute;left:235px;right:0;bottom:0;height:80px;background:linear-gradient(180deg,rgba(10,128,198,0) 0%,rgba(10,128,198,.85) 60%,#0a80c6 100%)}
.see-more{position:absolute;left:438px;bottom:28px;font-size:7px;font-weight:600;text-align:center}

/* resources */
.resources{height:350px;background:linear-gradient(180deg,#eef6fa,#ffffff 40%,#f0fbf1);display:flex;gap:12px;padding:65px 35px 0}
.res-card{width:186px;height:208px;border:1px solid #8fd6a0;border-radius:3px;background:var(--white);text-align:center;padding:16px 10px 0}
.res-card svg{width:26px;height:26px}
.res-card h3{font-size:8px;font-weight:700;margin-top:10px}
.res-card p{font-size:6.8px;line-height:13.5px;margin-top:28px}
.res-card .btn{margin-top:20px}
.res-info{flex:1;position:relative}
.res-info h2{font-size:14px;font-weight:700}
.res-info p{font-size:6.8px;line-height:13.5px;margin-top:8px;width:165px}
.res-doctor{position:absolute;left:25px;top:118px;width:150px;height:170px;background:linear-gradient(180deg,rgba(223,230,236,0),#d3dee7 40%,#b9cbd9)}

/* newsletter */
.newsletter{height:68px;background:var(--ink);display:flex;align-items:center;justify-content:space-between;padding:0 52px 0 35px;color:var(--white)}
.nl-left{display:flex;align-items:center;gap:14px}
.nl-icon{width:42px;height:36px;border-radius:6px;background:#2c2f33;display:flex;align-items:center;justify-content:center}
.nl-left p{font-size:10.5px;line-height:13.5px}
.nl-form{width:286px;height:26px;background:var(--white);border-radius:13px;display:flex;align-items:center;justify-content:space-between;padding:0 2px 0 10px}
.nl-form span{font-size:7px;color:#8a9097}
.nl-form .btn{padding:0 17px}

/* footer */
.site-footer{height:77px;background:linear-gradient(180deg,#fff,#eef5fa);padding:12px 32px 0}
.footer-row{display:flex;justify-content:space-between;align-items:center}
.footer-row .nav{gap:30px;margin-right:5px}
.footer-bar{display:flex;align-items:center;justify-content:space-between;margin-top:3px;padding-left:79px}
.bar{width:428px;height:13px;border-radius:7px;background:#000}
.socials{display:flex;gap:17px;margin-right:5px}
.socials span{width:10px;height:10px;border-radius:50%;background:var(--blue)}
.legal{text-align:center;font-size:5.5px;color:#9aa1a8;margin-top:14px}
</style>
</head>
<body>
<div class="page">

  <header class="site-header">
    <div class="brand"><span class="brand-dot"></span>K7VANT-Lab</div>
    <nav class="nav"><a>Home</a><a>About Us</a><a>Research Areas</a><a>Our Team</a><a>Contact</a></nav>
  </header>

  <section class="hero">
    <div class="hero-photo" role="img" aria-label="Photo of researchers working together at a laptop in a bright clinic office"></div>
    <div class="hero-text">
      <h1>Innovating for a Hopeful Future in Borderline Personality Disorder (BPD) Research</h1>
      <p>We are a team of researchers committed to developing innovative interventions to improve the lives of individuals with Borderline Personality Disorder through a science-based approach.</p>
      <div class="actions">
        <a class="btn btn-green">Meet Our Team</a>
        <a class="btn btn-blue">Explore Our Research</a>
      </div>
    </div>
  </section>

  <section class="about">
    <div class="about-photo" role="img" aria-label="Overhead photo of a medical team meeting around a white table"></div>
    <div class="about-body">
      <h2>About Us</h2>
      <p>Affiliated with TVOLBAE, our laboratory is dedicated to creating tomorrow's interventions to offer a hopeful future for individuals living with Borderline Personality Disorder</p>
      <div class="values">
        <div class="value">
          <svg viewBox="0 0 12 12" fill="#fff"><circle cx="6" cy="4.5" r="3.5"/><rect x="4.5" y="8.5" width="3" height="2.5" rx=".6"/></svg>
          Innovation
        </div>
        <div class="value">
          <svg viewBox="0 0 12 12" fill="#fff"><path d="M6 11V6C6 3 3 2 1 2.5 1 5 3 6.5 6 6Z"/><path d="M6 6C6 3.5 8.5 2 11 2.5 11 5 9 6.5 6 6Z"/><rect x="5.4" y="6" width="1.2" height="5"/></svg>
          Hope
        </div>
        <div class="value">
          <svg viewBox="0 0 12 12" fill="#fff"><path d="M7 1.5a1.6 1.6 0 0 1 2.5 0 1.6 1.6 0 0 1 2.2 2.2L9.3 6 7 3.7A1.6 1.6 0 0 1 7 1.5Z"/><rect x="1" y="5" width="2" height="6"/><path d="M3 9.5h4.5L11 7.5v1.5L8 11H3Z"/></svg>
          Empathy and<br>Personalization
        </div>
      </div>
      <a class="btn btn-dark">Learn More Our Mission</a>
    </div>
  </section>

  <section class="research">
    <h2>Our Research Areas</h2>
    <p class="lead">We are a team of researchers committed to developing innovative interventions to improve the lives of individuals with Borderline Personality Disorder through a science-based approach.</p>
    <a class="btn btn-blue">Learn More</a>
    <div class="areas">
      <article class="area active">
        <div class="area-art" role="img" aria-label="Illustration of two heads sharing a heart with a medical cross"></div>
        <h3>Lifestyle Medicine and BPD</h3>
        <p>Improving emotional regulation and overall health through lifestyle habits like sleep, nutrition, and physical activity.</p>
      </article>
      <article class="area">
        <div class="area-art" role="img" aria-label="Illustration of a head with a brain surrounded by connected nodes"></div>
        <h3>Interventions Supporting Psychosocial Functioning</h3>
        <p>Enhancing social and professional integration strategies for patients</p>
      </article>
      <article class="area">
        <div class="area-art" role="img" aria-label="Illustration of a head profile with a blue brain"></div>
        <h3>Optimization of Psychotherapeutic Strategies in BPD</h3>
        <p>Personalizing psychotherapeutic approaches for long-term impact</p>
      </article>
      <article class="area">
        <div class="area-art" role="img" aria-label="Illustration of a half-outlined, half-blue brain with small sparkles"></div>
        <h3>Neuromodulation and Pharmacotherapy</h3>
        <p>Exploring innovative biological treatments to improve BPD management</p>
      </article>
    </div>
  </section>

  <section class="team">
    <h2>Meet Our Team</h2>
    <div class="team-head">
      <p>Our team includes dedicated researchers and students who are passionate about advancing BPD research</p>
      <a class="btn btn-dark" style="padding:0 22px">See All
        <svg width="12" height="8" viewBox="0 0 12 8" fill="none" stroke="#fff"><path d="M0 4h11M8 1l3 3-3 3"/></svg></a>
    </div>
    <div class="members">
      <div class="member"><div class="shot" role="img" aria-label="Portrait photo of a doctor in a white coat" style="background:linear-gradient(180deg,#d9dde0,#c3cad0)"></div><div class="cap"><b>Arvin Castell</b><span>Doctor</span></div></div>
      <div class="member"><div class="shot" role="img" aria-label="Portrait photo of a doctor outdoors among trees" style="background:linear-gradient(180deg,#6e8a3c,#a8a070 60%,#e8e4dc)"></div><div class="cap"><b>Elena Varro</b><span>Doctor</span></div></div>
      <div class="member"><div class="shot" role="img" aria-label="Portrait photo of a doctor against a soft pink wall" style="background:linear-gradient(180deg,#e9d8dc,#e6e2e4)"></div><div class="cap"><b>Minh Tollan</b><span>Doctor</span></div></div>
      <div class="member"><div class="shot" role="img" aria-label="Portrait photo of a nurse in blue scrubs in a hospital corridor" style="background:linear-gradient(180deg,#c7ced4,#8aa6c0 60%,#2f6aa6)"></div><div class="cap"><b>Sonja Reyvel</b><span>Doctor</span></div></div>
    </div>
    <svg class="arrow" style="left:14px" viewBox="0 0 10 10" fill="none" stroke="#fff" stroke-width="1.2"><path d="M6.5 1.5L3 5l3.5 3.5"/></svg>
    <svg class="arrow" style="right:14px" viewBox="0 0 10 10" fill="none" stroke="#fff" stroke-width="1.2"><path d="M3.5 1.5L7 5 3.5 8.5"/></svg>
  </section>

  <section class="pubs">
    <div class="pubs-head">
      <h2>Latest Publications</h2>
      <a class="btn btn-blue" style="padding:0 22px">See All
        <svg width="12" height="8" viewBox="0 0 12 8" fill="none" stroke="#fff"><path d="M0 4h11M8 1l3 3-3 3"/></svg></a>
    </div>
    <div class="pub-grid">
      <article class="pub current"><h3>What is Borderline Personality Disorder (BPD)</h3><p>BPD is a mental health condition that affects emotions, relationships, and self-image. People with BPD often experience intense mood swings and difficulty managing their emotions.</p><a>Learn More <svg width="12" height="8" viewBox="0 0 12 8" fill="none" stroke="currentColor"><path d="M0 4h11M8 1l3 3-3 3"/></svg></a></article>
      <article class="pub"><h3>Common Symptoms of BPD</h3><p>Symptoms include emotional instability, fear of abandonment, impulsive behavior, and difficulty maintaining relationships. These can affect daily life and personal well-being.</p><a>Learn More <svg width="12" height="8" viewBox="0 0 12 8" fill="none" stroke="currentColor"><path d="M0 4h11M8 1l3 3-3 3"/></svg></a></article>
      <article class="pub"><h3>Causes and Risk Factors of BPD</h3><p>BPD can develop due to genetic factors, childhood trauma, or brain chemistry differences. It often begins in adolescence or early adulthood.</p><a>Learn More <svg width="12" height="8" viewBox="0 0 12 8" fill="none" stroke="currentColor"><path d="M0 4h11M8 1l3 3-3 3"/></svg></a></article>
      <article class="pub"><h3>How is BPD Diagnosed?</h3><p>A mental health professional diagnoses BPD based on emotional patterns, behaviors, and personal history. There is no single test, but therapy assessments help identify it.</p><a>Learn More <svg width="12" height="8" viewBox="0 0 12 8" fill="none" stroke="currentColor"><path d="M0 4h11M8 1l3 3-3 3"/></svg></a></article>
      <article class="pub"><h3>Treatment Options for BPD</h3><p>BPD can be managed with therapy, medication, and lifestyle changes. Dialectical Behavior Therapy (DBT) is one of the most effective treatments.</p><a>Learn More <svg width="12" height="8" viewBox="0 0 12 8" fill="none" stroke="currentColor"><path d="M0 4h11M8 1l3 3-3 3"/></svg></a></article>
      <article class="pub"><h3>Living with BPD: Support and Coping Strategies</h3><p>Managing BPD requires self-awareness, therapy, and a strong support system. Healthy habits, mindfulness, and professional guidance can improve daily life.</p><a>Learn More <svg width="12" height="8" viewBox="0 0 12 8" fill="none" stroke="currentColor"><path d="M0 4h11M8 1l3 3-3 3"/></svg></a></article>
    </div>
  </section>

  <section class="projects">
    <div class="projects-intro">
      <h2>Ongoing Projects</h2>
      <p>We are a team of researchers committed to developing innovative interventions to improve the lives of individuals with Borderline Personality Disorder through a science-based approach.</p>
    </div>
    <div class="doctor" role="img" aria-label="Photo of a smiling doctor in a white coat pointing toward the project list"></div>
    <div class="project-list">
      <article class="project">
        <div class="project-top"><b>Lifestyle Interventions for BPD</b><span class="k">Tittle</span><span class="v1">Ongprogress</span><span class="k">Status</span><span class="v2">Recruiting</span></div>
        <div class="project-body"><p>Exploring the impact of nutrition, sleep, and physical activity on emotional regulation in BPD patients. Currently recruiting participants for a 12-week study</p><a class="btn btn-green">Join This Study</a></div>
      </article>
      <article class="project short">
        <div class="project-top"><b>Psychotherapy Optimization</b><span class="k">Tittle</span><span class="v1">Ongprogress</span><span class="k">Status</span><span class="v2">Recruiting</span></div>
        <div class="project-body"><p>Evaluating personalized psychotherapeutic approaches to improve long-term outcomes for individuals with BPD. Recruitment for Phase 2 is now open.</p><a class="btn btn-green">Join This Study</a></div>
      </article>
      <article class="project short">
        <div class="project-top"><b>Neuromodulation Techniques</b><span class="k">Tittle</span><span class="v1">Ongprogress</span><span class="k">Status</span><span class="v2">Recruiting</span></div>
        <div class="project-body"><p>Investigating the effectiveness of transcranial magnetic stimulation (TMS) as a complementary treatment for BPD. Seeking volunteers for clinical trials.</p><a class="btn btn-green">Join This Study</a></div>
      </article>
      <article class="project short">
        <div class="project-top"><b>Neuromodulation Techniques</b><span class="k">Tittle</span><span class="v1">Ongprogress</span><span class="k">Status</span><span class="v2">Recruiting</span></div>
        <div class="project-body"><p>Investigating the effectiveness of transcranial magnetic stimulation (TMS) as a complementary treatment for BPD.</p><a class="btn btn-green">Join This Study</a></div>
      </article>
    </div>
    <div class="fade"></div>
    <div class="see-more">See More<br><svg width="10" height="6" viewBox="0 0 10 6" fill="none" stroke="#fff" stroke-width="1.2"><path d="M1 1l4 4 4-4"/></svg></div>
  </section>

  <section class="resources">
    <article class="res-card">
      <svg viewBox="0 0 26 26" fill="none" stroke="#111" stroke-width="1.6"><path d="M2 5h9l2 2 2-2h9v16h-9l-2 2-2-2H2z"/><path d="M13 7v16M16 11h5M16 15h5"/></svg>
      <h3>Student Resources</h3>
      <p>Access research guides, learning materials, and internship opportunities to support your academic and professional growth in BPD research.</p>
      <a class="btn btn-blue">Explore Student Resources</a>
    </article>
    <article class="res-card">
      <svg viewBox="0 0 26 26" fill="none" stroke="#111" stroke-width="1.6"><path d="M13 22C5 16 2 12 2 8a5 5 0 0 1 11-2 5 5 0 0 1 11 2c0 4-3 8-11 14z"/></svg>
      <h3>Patient Resources</h3>
      <p>Find helpful information, self-care tips, and community support to assist you or your loved ones in managing Borderline Personality Disorder</p>
      <a class="btn btn-blue">Explore Patient Resources</a>
    </article>
    <div class="res-info">
      <h2>Resources</h2>
      <p>xplore our curated collection of resources designed to support students and patients. Whether you're looking for research guides, learning materials, or self-care tips, we provide valuable tools to empower your journey.</p>
      <div class="res-doctor" role="img" aria-label="Photo of a doctor in a white coat holding a clipboard"></div>
    </div>
  </section>

  <section class="newsletter">
    <div class="nl-left">
      <div class="nl-icon"><svg width="22" height="16" viewBox="0 0 22 16" fill="none" stroke="#fff" stroke-width="1.4"><rect x="1" y="1" width="20" height="14" rx="2"/><path d="M1 2l10 7 10-7"/></svg></div>
      <p>For Lates Updates<br>Subscribe to Our Newsletter</p>
    </div>
    <div class="nl-form"><span>Enter your email</span><a class="btn btn-blue">Subscribe</a></div>
  </section>

  <footer class="site-footer">
    <div class="footer-row">
      <div class="brand"><span class="brand-dot"></span>K7VANT-Lab</div>
      <nav class="nav"><a>Home</a><a>About Us</a><a>Research Areas</a><a>Our Team</a><a>Contact</a></nav>
    </div>
    <div class="footer-bar">
      <div class="bar"></div>
      <div class="socials"><span></span><span></span><span></span></div>
    </div>
    <p class="legal">K7VANT-Lab © 2025 &nbsp;·&nbsp; Research team working on personality disorders</p>
  </footer>

</div>
</body>
</html>
```